Dean harlow realestate

We want something complete different to our website now and something that will stand out this is our website http://deanharlowrealestate-example.com/

our company website for my boss is www.trevorvance-example.com

please note this website is being made for dean harlow not trevor vance

something similar to our company website but has to be in the branding of dean harlow realestate

```html
<!DOCTYPE html>
<html lang="en">
<head>
<meta charset="utf-8">
<title>Dean Harlow Property</title>
<link href="https://fonts.googleapis.com/css2?family=Open+Sans:wght@400;600&family=Roboto+Condensed:wght@400;700&display=swap" rel="stylesheet">
<style>
:root{
  --orange:#e8762b;
  --orange-dark:#d9641c;
  --navy:#1b2550;
  --navy-deep:#151d42;
  --price:#e0452b;
  --ink:#333;
  --muted:#777;
  --line:#d8d8d8;
  --footer:#121212;
  --white:#fff;
}
*{box-sizing:border-box;margin:0;padding:0}
html,body{width:1200px;height:3629px;overflow:hidden}
body{position:relative;font-family:"Open Sans",Arial,sans-serif;color:var(--ink);background:var(--white)}
.abs{position:absolute}
.cond{font-family:"Roboto Condensed","Arial Narrow",sans-serif}

/* header */
.site-header{left:0;top:0;width:1200px;height:102px;border-top:5px solid var(--orange);background:var(--white)}
.brand{left:86px;top:26px;height:46px;padding:0 14px;background:#f1f1f1;font-size:30px;line-height:46px;color:#222}
.main-nav{right:100px;top:38px;display:flex;gap:38px;font-size:17px;color:#222}
.main-nav .phone{display:flex;align-items:center;gap:10px}

/* hero */
.hero{left:0;top:102px;width:1200px;height:515px;background:linear-gradient(100deg,#2a3a2c 0%,#4d6a3e 35%,#7f9a6a 60%,#5e7660 80%,#8a9aa0 100%)}
.hero-partner{left:22px;top:112px;color:var(--white);font-size:11px;display:flex;flex-direction:column;align-items:flex-start;gap:6px}
.hero-partner .sq{width:24px;height:24px;background:var(--orange)}
.hero-title{left:668px;top:274px;width:376px;height:172px;border:2px solid rgba(255,255,255,.7);background:rgba(0,0,0,.55);color:var(--white);text-align:center;padding-top:26px}
.hero-title .t1{font-size:52px;line-height:58px}
.hero-title .t2{font-size:46px;line-height:52px}
.watch{left:775px;top:470px;display:flex;align-items:center;gap:16px;color:var(--white);font-size:17px}
.hero-dots{left:1070px;top:578px;color:#ddd;font-size:16px;letter-spacing:12px}
.swoosh{left:0;top:600px}

/* listings */
.section-title{font-size:27px;color:#111}
.listings-title{left:90px;top:700px}
.card{left:90px;width:685px;height:240px;background:var(--white);box-shadow:0 2px 8px rgba(0,0,0,.2);padding:30px 20px}
.card .photo{position:absolute;left:18px;top:28px;width:216px;height:186px}
.card .body{position:absolute;left:247px;top:30px;width:420px}
.sold{display:inline-block;background:var(--orange);color:var(--white);font-size:14px;padding:2px 13px}
.card h3{font-weight:400;font-size:17px;margin:12px 0 6px;color:#222}
.card p{font-size:13.5px;line-height:22px;color:#555}
.price{color:var(--price);font-size:19px;margin:10px 0 10px}
.meta{display:flex;align-items:center;gap:10px;font-size:14px;color:#666}
.meta svg{fill:#777}

.pagination{left:94px;top:2026px;display:flex;gap:8px}
.pagination span{border:1px solid #ccc;font-size:12px;padding:3px 10px;color:#333;background:#fafafa}
.pagination .on{background:var(--orange);border-color:var(--orange);color:var(--white)}

/* sidebar */
.appraisal{left:796px;top:765px;width:317px;height:554px;background:var(--navy);padding:22px 30px}
.appraisal h2{color:var(--white);font-weight:400;font-size:26px;text-align:center;margin-bottom:16px}
.field{background:var(--white);height:43px;margin-bottom:12px;font-size:13px;padding:12px 10px;color:#333}
.field.tall{height:96px}
.btn-send{background:var(--orange);color:var(--white);text-align:center;font-size:22px;height:46px;line-height:46px;margin-top:6px}
.promo{left:796px;width:317px;color:var(--white);overflow:hidden}
.promo-sale{top:1338px;height:319px;background:linear-gradient(180deg,#2d3f6a 0%,#56628a 35%,#9a7a5a 75%,#5a4a3a 100%)}
.promo-sale .label{position:absolute;left:0;width:100%;text-align:center;top:28px;font-size:24px}
.promo-sale .cut{position:absolute;right:0;bottom:0}
.promo-sale .corner{position:absolute;right:24px;bottom:26px;text-align:right;font-size:24px;line-height:30px}
.promo-video{top:1682px;height:322px;background:linear-gradient(180deg,#3a4648 0%,#6c705a 45%,#4a4236 100%)}
.promo-video .play{position:absolute;left:130px;top:100px}
.promo-video .label{position:absolute;left:0;width:100%;text-align:center;top:236px;font-size:28px}

/* testimonials */
.testimonials{left:0;top:2139px;width:1200px;height:566px;background:var(--navy-deep)}
.testimonials h2{position:absolute;left:0;width:100%;text-align:center;top:76px;color:var(--white);font-weight:400;font-size:29px}
.quote{background:var(--white);border-radius:10px;padding:30px 24px;font-size:14px;line-height:22px;color:#333}
.quote.featured{background:var(--orange);color:var(--white)}
.quote .qm{position:absolute;left:20px;top:26px}
.quote .stars{color:var(--orange);text-align:center;letter-spacing:4px;margin-top:10px;font-size:18px}
.quote.featured .stars{color:var(--white)}
.avatar{width:72px;height:72px;border-radius:50%;background:#cfd3d8;border:4px solid var(--white)}
.client{color:var(--white);text-align:center;font-size:14px;line-height:18px}

/* contact */
.contact-title{left:0;width:1200px;text-align:center;top:2818px;font-size:27px;color:#111}
.footer{left:0;top:3090px;width:1200px;height:539px;background:var(--footer)}
.contact-box{left:140px;top:2887px;width:932px;height:392px;background:var(--white);border:1px solid #ccc}
.quick{position:absolute;left:56px;top:26px;width:330px}
.quick h3{font-weight:400;font-size:25px;margin-bottom:14px;color:#222}
.quick .field{border:1px solid #999;height:43px;margin-bottom:6px;padding:11px 10px}
.quick .field.tall{height:80px}
.quick .send{display:inline-block;background:var(--orange);color:var(--white);border-radius:20px;padding:8px 30px;font-size:15px;margin-top:8px}
.map{position:absolute;left:446px;top:0;width:486px;height:390px;background:linear-gradient(135deg,#e6e6e6,#cfcfcf)}
.map .pin{position:absolute;left:224px;top:146px}

.fcol{color:var(--white);font-size:14px;line-height:24px}
.fcol h4{font-weight:400;font-size:15px;margin-bottom:22px;letter-spacing:.5px}
.fcol ul{list-style:none}
.fcol li::before{content:"» "}
.ci{display:flex;align-items:flex-start;gap:12px;margin-bottom:8px}
.ci svg{flex:0 0 auto;margin-top:3px}
.subscribe{margin-top:26px;width:218px;height:44px;border:1px solid #bbb;border-radius:22px;display:flex;align-items:center;justify-content:space-between;padding:0 14px 0 22px;font-size:13px;color:#ccc}
.footer-rule{left:96px;top:3535px;width:1010px;height:1px;background:#444}
.copyright{left:0;width:1200px;text-align:center;top:3567px;color:var(--white);font-size:13px}
</style>
</head>
<body>

<header class="site-header abs">
  <div class="brand abs">Dean Harlow Property</div>
  <nav class="main-nav abs">
    <span>Home</span><span>For sale</span><span>Agents</span><span>Book appraisal</span><span>Contact</span>
    <span class="phone"><svg width="16" height="16" viewBox="0 0 24 24"><path fill="#e8762b" d="M6.6 10.8a15 15 0 0 0 6.6 6.6l2.2-2.2c.3-.3.7-.4 1-.2 1.1.4 2.3.6 3.6.6.6 0 1 .4 1 1V20c0 .6-.4 1-1 1A17 17 0 0 1 3 4c0-.6.4-1 1-1h3.5c.6 0 1 .4 1 1 0 1.3.2 2.5.6 3.6.1.3 0 .7-.2 1z"/></svg>0400 318 627</span>
  </nav>
</header>

<section class="hero abs" role="img" aria-label="Video still of the agent speaking outdoors in front of trees and parked cars"></section>
<div class="hero-partner abs"><span class="sq"></span><span>TREVOR VANCE</span></div>
<div class="hero-title abs cond"><div class="t1">Dean Harlow</div><div class="t2">Property</div></div>
<div class="watch abs"><svg width="44" height="44" viewBox="0 0 44 44"><circle cx="22" cy="22" r="21" fill="#fff"/><path d="M17 13l13 9-13 9z" fill="#e8762b"/></svg>WATCH VIDEO</div>
<div class="hero-dots abs">‹ ›</div>
<svg class="swoosh abs" width="1200" height="60" viewBox="0 0 1200 60"><path d="M0 17 L0 17 Q600 10 1200 0 L1200 58 Q700 30 0 17Z" fill="#e8762b"/><path d="M0 17 L1200 0 L1200 18 Q600 14 0 17Z" fill="#fff"/></svg>

<h2 class="section-title listings-title abs cond">LATEST PROPERTIES FOR SALE</h2>

<article class="card abs" style="top:762px">
  <div class="photo" role="img" aria-label="Single-storey white house with grey roof under blue sky" style="background:linear-gradient(180deg,#6fa1d8 0%,#b8cde4 45%,#d9d9d4 60%,#8a8a86 100%)"></div>
  <div class="body"><span class="sold">Sold</span><h3>18 marlow street kewale, 6105</h3><p>It is a long established fact that a reader will be distracted by the readable content of a page when looking at its layout.</p><div class="price">FROM $689,000</div>
  <div class="meta">House <svg width="18" height="12" viewBox="0 0 18 12"><path d="M0 0h2v6h16v6h-2v-3H2v3H0zM3 3h4v3H3zm5 1h9v2H8z"/></svg>4 <svg width="18" height="12" viewBox="0 0 18 12"><path d="M0 5h18v2c0 2-2 4-5 4H5C2 11 0 9 0 7zM2 0h3v4H2z"/></svg>2 <svg width="18" height="12" viewBox="0 0 18 12"><path d="M3 1h12l2 5v5h-3v-2H4v2H1V6zm1 4h10l-1-3H5z"/></svg>2</div></div>
</article>
<article class="card abs" style="top:1014px">
  <div class="photo" role="img" aria-label="Two-storey red brick house with white garage door" style="background:linear-gradient(180deg,#5e95d6 0%,#a3c0e3 35%,#a0523a 55%,#8a4a36 80%,#c9c3b8 100%)"></div>
  <div class="body"><span class="sold">Sold</span><h3>18 marlow street kewale, 6105</h3><p>It is a long established fact that a reader will be distracted by the readable content of a page when looking at its layout.</p><div class="price">FROM $689,000</div>
  <div class="meta">House <svg width="18" height="12" viewBox="0 0 18 12"><path d="M0 0h2v6h16v6h-2v-3H2v3H0zM3 3h4v3H3zm5 1h9v2H8z"/></svg>4 <svg width="18" height="12" viewBox="0 0 18 12"><path d="M0 5h18v2c0 2-2 4-5 4H5C2 11 0 9 0 7zM2 0h3v4H2z"/></svg>2 <svg width="18" height="12" viewBox="0 0 18 12"><path d="M3 1h12l2 5v5h-3v-2H4v2H1V6zm1 4h10l-1-3H5z"/></svg>2</div></div>
</article>
<article class="card abs" style="top:1266px">
  <div class="photo" role="img" aria-label="Brick house with tiled roof and small front garden" style="background:linear-gradient(180deg,#4f86c9 0%,#9bbde0 35%,#b27a55 60%,#9a6e50 80%,#d4c6b2 100%)"></div>
  <div class="body"><span class="sold">Sold</span><h3>18 marlow street kewale, 6105</h3><p>It is a long established fact that a reader will be distracted by the readable content of a page when looking at its layout.</p><div class="price">FROM $689,000</div>
  <div class="meta">House <svg width="18" height="12" viewBox="0 0 18 12"><path d="M0 0h2v6h16v6h-2v-3H2v3H0zM3 3h4v3H3zm5 1h9v2H8z"/></svg>4 <svg width="18" height="12" viewBox="0 0 18 12"><path d="M0 5h18v2c0 2-2 4-5 4H5C2 11 0 9 0 7zM2 0h3v4H2z"/></svg>2 <svg width="18" height="12" viewBox="0 0 18 12"><path d="M3 1h12l2 5v5h-3v-2H4v2H1V6zm1 4h10l-1-3H5z"/></svg>2</div></div>
</article>
<article class="card abs" style="top:1518px">
  <div class="photo" role="img" aria-label="House at dusk with lit windows behind a dark gate" style="background:linear-gradient(180deg,#2c3550 0%,#5a5a5a 40%,#8a6a4a 60%,#3a3430 100%)"></div>
  <div class="body"><span class="sold">Sold</span><h3>18 marlow street kewale, 6105</h3><p>It is a long established fact that a reader will be distracted by the readable content of a page when looking at its layout.</p><div class="price">FROM $689,000</div>
  <div class="meta">House <svg width="18" height="12" viewBox="0 0 18 12"><path d="M0 0h2v6h16v6h-2v-3H2v3H0zM3 3h4v3H3zm5 1h9v2H8z"/></svg>4 <svg width="18" height="12" viewBox="0 0 18 12"><path d="M0 5h18v2c0 2-2 4-5 4H5C2 11 0 9 0 7zM2 0h3v4H2z"/></svg>2 <svg width="18" height="12" viewBox="0 0 18 12"><path d="M3 1h12l2 5v5h-3v-2H4v2H1V6zm1 4h10l-1-3H5z"/></svg>2</div></div>
</article>
<article class="card abs" style="top:1770px">
  <div class="photo" role="img" aria-label="Modern white two-storey house with grey garage door" style="background:linear-gradient(180deg,#aac6e6 0%,#e6e8ea 40%,#bfc2c4 65%,#7d8082 100%)"></div>
  <div class="body"><span class="sold">Sold</span><h3>18 marlow street kewale, 6105</h3><p>It is a long established fact that a reader will be distracted by the readable content of a page when looking at its layout.</p><div class="price">FROM $689,000</div>
  <div class="meta">House <svg width="18" height="12" viewBox="0 0 18 12"><path d="M0 0h2v6h16v6h-2v-3H2v3H0zM3 3h4v3H3zm5 1h9v2H8z"/></svg>4 <svg width="18" height="12" viewBox="0 0 18 12"><path d="M0 5h18v2c0 2-2 4-5 4H5C2 11 0 9 0 7zM2 0h3v4H2z"/></svg>2 <svg width="18" height="12" viewBox="0 0 18 12"><path d="M3 1h12l2 5v5h-3v-2H4v2H1V6zm1 4h10l-1-3H5z"/></svg>2</div></div>
</article>

<nav class="pagination abs"><span>Prev</span><span class="on">1</span><span>2</span><span>3</span><span>4</span><span>5</span><span>6</span><span>...</span><span>22</span><span>Next</span></nav>

<aside class="appraisal abs">
  <h2 class="cond">BOOK AN APPRAISAL</h2>
  <div class="field">Name</div><div class="field">Email</div><div class="field">Phone</div><div class="field">Address</div><div class="field">Preferred Time/Day</div><div class="field tall">Message</div>
  <div class="btn-send cond">Send</div>
</aside>

<div class="promo promo-sale abs cond" role="img" aria-label="Large house lit at twilight">
  <div class="label">Dean Harlow Property</div>
  <svg class="cut" width="317" height="150" viewBox="0 0 317 150"><path d="M317 0 L317 150 L0 150Z" fill="#e8762b"/></svg>
  <div class="corner">Properties<br>For sale</div>
</div>
<div class="promo promo-video abs cond" role="img" aria-label="Two-storey home exterior at dusk, video thumbnail">
  <svg class="play" width="58" height="58" viewBox="0 0 58 58"><circle cx="29" cy="29" r="29" fill="rgba(0,0,0,.6)"/><path d="M23 17l17 12-17 12z" fill="#fff"/></svg>
  <div class="label">Dean Harlow Property</div>
</div>

<section class="testimonials abs">
  <h2 class="cond">WHAT OUR CLIENTS THINK</h2>
</section>
<div class="quote abs" style="left:90px;top:2323px;width:309px;height:218px;padding-left:60px">
  <svg class="qm" width="34" height="22" viewBox="0 0 34 22"><path d="M0 10a9 9 0 0 1 14-7v2a6 6 0 0 0-5 5 5 5 0 1 1-9 0zm18 0a9 9 0 0 1 14-7v2a6 6 0 0 0-5 5 5 5 0 1 1-9 0z" fill="#e8762b"/></svg>
  We bought our first home through Dean and the process was easy and very straight forward. We felt confident buying our first home and extremely supported.
  <div class="stars">★★★★★</div>
</div>
<div class="quote featured abs" style="left:436px;top:2306px;width:334px;height:252px;padding-left:56px">
  <svg class="qm" width="34" height="22" viewBox="0 0 34 22"><path d="M0 10a9 9 0 0 1 14-7v2a6 6 0 0 0-5 5 5 5 0 1 1-9 0zm18 0a9 9 0 0 1 14-7v2a6 6 0 0 0-5 5 5 5 0 1 1-9 0z" fill="#fff"/></svg>
  I found Dean to be different from most agents, in that he listened, and set a marketing program to suit the special features of our property. Eager to do anything to assist with a positive outcome, I'd recommend Dean for properties
  <div class="stars">★★★★★</div>
</div>
<div class="quote abs" style="left:801px;top:2323px;width:312px;height:218px;padding-left:62px">
  <svg class="qm" width="34" height="22" viewBox="0 0 34 22"><path d="M0 10a9 9 0 0 1 14-7v2a6 6 0 0 0-5 5 5 5 0 1 1-9 0zm18 0a9 9 0 0 1 14-7v2a6 6 0 0 0-5 5 5 5 0 1 1-9 0z" fill="#e8762b"/></svg>
  Dean is very talented and highly ethical person who provides a high standard of customer service both during the transaction and after. Dean is very talented
  <div class="stars">★★★★★</div>
</div>
<div class="avatar abs" role="img" aria-label="Client portrait" style="left:212px;top:2500px"></div>
<div class="avatar abs" role="img" aria-label="Client portrait" style="left:566px;top:2518px"></div>
<div class="avatar abs" role="img" aria-label="Client portrait" style="left:922px;top:2500px"></div>
<div class="client abs" style="left:148px;top:2580px;width:200px">- Clara &amp; Mateo<br>Kewdale, 6105</div>
<div class="client abs" style="left:503px;top:2600px;width:200px;font-size:16px;line-height:22px">- Owen<br>Lathlain, 6100</div>
<div class="client abs" style="left:858px;top:2580px;width:200px">- Felix<br>Rivervale, 6103</div>

<h2 class="contact-title abs cond">CONTACT US</h2>
<footer class="footer abs"></footer>
<div class="contact-box abs">
  <div class="quick">
    <h3>Quick Contact</h3>
    <div class="field">Name</div><div class="field">Phone number</div><div class="field">Email address</div><div class="field tall">Message</div>
    <span class="send">SEND</span>
  </div>
  <div class="map" role="img" aria-label="Street map around the office location">
    <svg class="pin" width="40" height="56" viewBox="0 0 40 56"><path d="M20 0a20 20 0 0 1 20 20c0 15-20 36-20 36S0 35 0 20A20 20 0 0 1 20 0z" fill="#e0452b"/><circle cx="20" cy="20" r="7" fill="#fff"/></svg>
  </div>
</div>

<div class="fcol abs" style="left:145px;top:3330px">
  <h4>INFORMATION</h4>
  <ul><li>Privacy Policy</li><li>Book appraisal</li><li>For sale</li><li>Agents</li></ul>
</div>
<div class="fcol abs" style="left:465px;top:3330px;width:290px">
  <h4>CONTACT US</h4>
  <div class="ci"><svg width="20" height="20" viewBox="0 0 20 20"><circle cx="10" cy="10" r="10" fill="#fff"/><path d="M10 4a4 4 0 0 1 4 4c0 3-4 8-4 8S6 11 6 8a4 4 0 0 1 4-4z" fill="#121212"/></svg><span>Suite 14, 22 Ellery Road, Rivervale, WA 6103 Australia</span></div>
  <div class="ci"><svg width="20" height="20" viewBox="0 0 20 20"><circle cx="10" cy="10" r="10" fill="#fff"/><path d="M7 5l2 3-1 1a7 7 0 0 0 3 3l1-1 3 2-1 2c-4 0-9-5-9-9z" fill="#121212"/></svg><span>0400 318 627</span></div>
  <div class="ci"><svg width="20" height="20" viewBox="0 0 20 20"><circle cx="10" cy="10" r="10" fill="#fff"/><path d="M5 6h10v8H5zm0 0l5 4 5-4" fill="none" stroke="#121212" stroke-width="1.4"/></svg><span>dean@trevorvance-example.com</span></div>
</div>
<div class="fcol abs" style="left:850px;top:3330px;width:240px">
  <h4>JOIN OUR MAILING LIST</h4>
  <div>Your about us information would fit here nicely.</div>
  <div class="subscribe"><span>Email address</span><svg width="16" height="16" viewBox="0 0 16 16"><circle cx="8" cy="8" r="8" fill="#fff"/><path d="M8 4v8M4 8h8" stroke="#121212" stroke-width="2"/></svg></div>
</div>
<div class="footer-rule abs"></div>
<div class="copyright abs">Copyright © 2018. All Rights Reserved</div>

</body>
</html>
```